Flyer Design

MALLOWBYS, fish & Chips . 17 Fennick Lane, Chessington KT4 7RD, TEL; 0208 6142937
This is a existing business of Fish and Chips, would like to use picture of fish & Chips and the menu on the other side

Industry/Entity Type

Business

```html
<!DOCTYPE html>
<html lang="en">
<head>
<meta charset="utf-8">
<title>Mallowbys Fish &amp; Chips – Flyer</title>
<link rel="stylesheet" href="https://fonts.googleapis.com/css2?family=Exo+2:wght@400;800&family=Great+Vibes&family=Tinos&display=swap">
<style>
  :root {
    --backdrop: #a3121a;
    --ink: #1b1b1b;
    --lime: #b5d11d;
    --lime-text: #c4dc3a;
    --white: #ffffff;
  }
  * { box-sizing: border-box; margin: 0; padding: 0; }
  html, body { width: 1200px; height: 599px; overflow: hidden; }
  body {
    background: var(--backdrop);
    font-family: "Exo 2", Arial, sans-serif;
    position: relative;
  }
  .flyer-page {
    position: absolute;
    top: 88px;
    width: 560px;
    height: 422px;
    overflow: hidden;
    background: var(--ink);
    box-shadow: 0 6px 18px rgba(0,0,0,.35);
  }
  .flyer-front { left: 30px; }
  .flyer-back  { left: 610px; }

  .photo { position: absolute; }

  /* Front */
  .front-photos { position: absolute; inset: 0; }
  .brand-header {
    position: absolute; left: 322px; top: 0; width: 238px; height: 110px;
    background: var(--lime);
    text-align: center;
    padding-top: 34px;
    color: var(--ink);
  }
  .brand-name {
    font-weight: 800;
    font-size: 33px;
    line-height: 1;
    letter-spacing: 0.5px;
    white-space: nowrap;
  }
  .brand-tagline {
    font-weight: 400;
    font-size: 22px;
    line-height: 1;
    letter-spacing: 2px;
    margin-top: 6px;
    white-space: nowrap;
  }
  .contact-band {
    position: absolute; left: 322px; top: 110px; width: 238px; height: 36px;
    background: var(--ink);
    color: var(--white);
    font-size: 10.5px;
    text-align: center;
    padding-top: 4px;
    line-height: 14px;
  }
  .contact-line { display: flex; align-items: center; justify-content: center; gap: 4px; white-space: nowrap; }
  .contact-icon { width: 9px; height: 9px; flex: none; }

  /* Back */
  .menu-box {
    position: absolute; left: 0; top: 0; width: 302px; height: 185px;
    background: var(--ink);
    padding: 40px 20px 0 20px;
  }
  .menu-heading {
    display: flex; align-items: flex-end; gap: 4px;
    color: var(--lime-text);
    font-family: "Great Vibes", cursive;
    font-weight: 400;
    font-size: 30px;
    line-height: 1;
    margin-bottom: 6px;
  }
  .menu-heading::after {
    content: ""; flex: 1; height: 1px; background: #777; margin-bottom: 4px; margin-right: -18px;
  }
  .price-list { list-style: none; font-family: "Tinos", serif; color: var(--lime-text); font-size: 10.5px; }
  .price-item { display: flex; align-items: baseline; height: 17px; white-space: nowrap; }
  .price-item .leader { flex: 1; border-bottom: 1px dotted currentColor; margin: 0 2px; transform: translateY(-3px); }

  .sides-box {
    position: absolute; left: 302px; top: 185px; width: 258px; height: 237px;
    background: var(--ink);
    padding: 14px 16px 0 14px;
  }
  .sides-box .price-list { font-size: 11px; }
  .sides-box .price-item { height: 21px; }
  .back-brand { color: var(--white); margin-top: 6px; }
  .back-brand .brand-name { font-size: 35px; }
  .back-brand .brand-tagline {
    font-size: 21px; letter-spacing: 2.5px; margin-top: 2px;
    border-top: 1px solid var(--white); padding-top: 2px; display: inline-block;
  }
  .phone-bar {
    position: absolute; left: 0; right: 0; top: 200px;
    display: flex; align-items: center; height: 22px;
  }
  .phone-bar .bar { background: var(--lime); height: 12px; }
  .phone-bar .bar-start { width: 42px; }
  .phone-bar .bar-end { flex: 1; }
  .phone-number {
    display: flex; align-items: center; gap: 6px;
    color: var(--white); font-size: 18px; line-height: 1; padding: 0 8px 0 12px;
    white-space: nowrap;
  }
  .phone-icon { width: 16px; height: 16px; flex: none; }
</style>
</head>
<body>

<section class="flyer-page flyer-front" aria-label="Front of flyer">
  <svg class="front-photos" width="560" height="422" viewBox="0 0 560 422">
    <defs>
      <radialGradient id="fishPlate" cx="35%" cy="60%" r="70%">
        <stop offset="0" stop-color="#7f8a8c"/>
        <stop offset=".45" stop-color="#d6d9d6"/>
        <stop offset="1" stop-color="#f4f4f0"/>
      </radialGradient>
      <linearGradient id="chipsBowl" x1="0" y1="0" x2="1" y2="1">
        <stop offset="0" stop-color="#f6da74"/>
        <stop offset=".6" stop-color="#eec24c"/>
        <stop offset="1" stop-color="#a8763a"/>
      </linearGradient>
    </defs>
    <rect role="img" aria-label="Photo of grilled whole fish with lemon and tomato on a white plate, olive oil behind" x="0" y="0" width="340" height="422" fill="url(#fishPlate)"/>
    <path role="img" aria-label="Photo of a wooden bowl of crisp golden chips" d="M322 146 H560 V422 H292 Q352 300 322 146 Z" fill="url(#chipsBowl)"/>
  </svg>

  <header class="brand-header">
    <div class="brand-name">MALLOWBYS</div>
    <div class="brand-tagline">FISH &amp; CHIPS</div>
  </header>

  <div class="contact-band">
    <p class="contact-line">
      <svg class="contact-icon" viewBox="0 0 10 10" aria-hidden="true"><circle cx="5" cy="5" r="5" fill="#fff"/><path d="M5 2.2a1.9 1.9 0 0 0-1.9 1.9C3.1 5.6 5 7.8 5 7.8s1.9-2.2 1.9-3.7A1.9 1.9 0 0 0 5 2.2z" fill="#1b1b1b"/></svg>
      17 Fennick Lane, Chessington KT4 7RD
    </p>
    <p class="contact-line">
      <svg class="contact-icon" viewBox="0 0 10 10" aria-hidden="true"><circle cx="5" cy="5" r="5" fill="#fff"/><path d="M3.4 2.4l1 1.2-.5.7c.3.7.9 1.3 1.6 1.6l.7-.5 1.2 1-.6.9C5 7.2 2.8 5 2.6 3z" fill="#1b1b1b"/></svg>
      0208 6142937
    </p>
  </div>
</section>

<section class="flyer-page flyer-back" aria-label="Back of flyer with menu">
  <svg class="photo" style="left:302px;top:0" width="258" height="185" viewBox="0 0 258 185">
    <defs>
      <linearGradient id="chipsDip" x1="0" y1="0" x2="1" y2="1">
        <stop offset="0" stop-color="#f3d36a"/>
        <stop offset=".55" stop-color="#e7bd57"/>
        <stop offset="1" stop-color="#8f6a3a"/>
      </linearGradient>
    </defs>
    <rect role="img" aria-label="Photo of chips in a wooden bowl with salsa and lime" width="258" height="185" fill="url(#chipsDip)"/>
  </svg>

  <svg class="photo" style="left:0;top:185px" width="302" height="237" viewBox="0 0 302 237">
    <defs>
      <linearGradient id="salmonBoard" x1="0" y1="0" x2="1" y2="1">
        <stop offset="0" stop-color="#f7e6c4"/>
        <stop offset=".45" stop-color="#f2a27f"/>
        <stop offset="1" stop-color="#d79a5e"/>
      </linearGradient>
    </defs>
    <rect role="img" aria-label="Photo of a raw salmon steak with dill on a wooden board" width="302" height="237" fill="url(#salmonBoard)"/>
  </svg>

  <div class="menu-box">
    <h2 class="menu-heading">Menu</h2>
    <ul class="price-list">
      <li class="price-item"><span>Fish</span><span class="leader"></span><span>$20</span></li>
      <li class="price-item"><span>Fish Fry</span><span class="leader"></span><span>$30</span></li>
      <li class="price-item"><span>Fish Curry</span><span class="leader"></span><span>$40</span></li>
      <li class="price-item"><span>Fish Dry Fry</span><span class="leader"></span><span>$25</span></li>
      <li class="price-item"><span>Fish</span><span class="leader"></span><span>$20</span></li>
      <li class="price-item"><span>Fish Fry</span><span class="leader"></span><span>$30</span></li>
    </ul>
  </div>

  <div class="sides-box">
    <ul class="price-list">
      <li class="price-item"><span>Potato Chips</span><span class="leader"></span><span>$10</span></li>
      <li class="price-item"><span>Potato Chips</span><span class="leader"></span><span>$10</span></li>
      <li class="price-item"><span>Potato Chips</span><span class="leader"></span><span>$10</span></li>
      <li class="price-item"><span>Potato Chips</span><span class="leader"></span><span>$10</span></li>
      <li class="price-item"><span>Potato Chips</span><span class="leader"></span><span>$10</span></li>
    </ul>
    <div class="back-brand">
      <div class="brand-name">MALLOWBYS</div>
      <div class="brand-tagline">FISH &amp; CHIPS</div>
    </div>
    <div class="phone-bar">
      <span class="bar bar-start"></span>
      <span class="phone-number">
        <svg class="phone-icon" viewBox="0 0 16 16" aria-hidden="true"><circle cx="8" cy="8" r="8" fill="#fff"/><path d="M5.3 3.6l1.7 2-.8 1.1c.5 1.2 1.5 2.2 2.7 2.7l1.1-.8 2 1.7-1 1.4C7.8 11.6 4.4 8.2 4 5z" fill="#1b1b1b"/></svg>
        0208 6142937
      </span>
      <span class="bar bar-end"></span>
    </div>
  </div>
</section>

</body>
</html>
```